Halloway Crest Backers Guild business cards

Create a single-sided business card for the Halloway Crest Backers Guild based on the attached logo.
The additional data fields include Name, Title, Email, Phone, and website.
Please use the following as sample data:
Name: Dean Varrow
Title: Co-Founder / Investor
Email: deanvarrow@mailtern.net
Phone: 555-314-2706
Website: www.hcbackersguild.com

Target Market(s)

Start ups, entrepreneurs, venture capitalists

Industry/Entity Type

Investment

Contact Information for Business Card

Professional business card. Technology company.

Font styles to use
Serif
Sans Serif

Requirements
Must have
• Include the HCBG logo (attached)
• Name
• Title
• Email
• Phone
• Website
Should not have
• Cute, cartoony

```html
<!DOCTYPE html>
<html lang="en">
<head>
<meta charset="utf-8">
<title>Halloway Crest Backers Guild – Business Card</title>
<link href="https://fonts.googleapis.com/css2?family=Open+Sans:wght@300;400;600;700&display=swap" rel="stylesheet">
<style>
  :root {
    --brand-green: #1f8a47;
    --ink-dark: #3a3a3c;
    --ink-grey: #555558;
    --paper: #ffffff;
    --backdrop: #ecebe8;
  }
  * { box-sizing: border-box; margin: 0; padding: 0; }
  html, body {
    width: 1200px; height: 900px; overflow: hidden;
    background: var(--backdrop);
    font-family: "Open Sans", Arial, sans-serif;
  }
  .canvas { position: relative; width: 1200px; height: 900px; }
  .card {
    position: absolute; width: 520px; height: 297px;
    box-shadow: 0 10px 28px rgba(0,0,0,0.18);
    overflow: hidden;
  }

  /* Front */
  .card-front { left: 70px; top: 140px; background: var(--brand-green); }
  .front-mark {
    position: absolute; left: 104px; top: 124px;
    width: 48px; height: 48px; border-radius: 50%; background: var(--paper);
  }
  .front-divider {
    position: absolute; left: 196px; top: 92px;
    width: 1px; height: 112px; background: rgba(255,255,255,0.85);
  }
  .front-name { position: absolute; left: 214px; top: 104px; color: var(--paper); }
  .front-name .line-top { font-weight: 300; font-size: 33px; line-height: 1.1; letter-spacing: 0.5px; }
  .front-name .line-bottom { font-weight: 700; font-size: 16px; letter-spacing: 4.2px; margin-top: 4px; }

  /* Back */
  .card-back { left: 610px; top: 460px; background: var(--paper); }
  .back-wave { position: absolute; left: 0; top: 0; width: 520px; height: 297px; }
  .holder { position: absolute; left: 34px; top: 62px; }
  .holder-name { color: var(--brand-green); font-weight: 700; font-size: 17px; letter-spacing: 0.3px; }
  .holder-title { color: var(--ink-grey); font-size: 12px; margin-top: 1px; }

  .back-brand {
    position: absolute; right: 30px; top: 34px; width: 150px;
    display: flex; align-items: flex-start; gap: 8px;
  }
  .back-brand .dot { flex: none; width: 14px; height: 14px; border-radius: 50%; background: var(--brand-green); margin-top: 2px; }
  .back-brand .label { color: var(--brand-green); font-weight: 600; font-size: 12px; line-height: 1.3; }

  .contact-list { position: absolute; left: 40px; top: 152px; list-style: none; }
  .contact-list li {
    display: flex; align-items: center; gap: 7px;
    color: var(--ink-dark); font-size: 13px; line-height: 19px;
  }
  .contact-list svg { width: 10px; height: 10px; flex: none; }
</style>
</head>
<body>
<main class="canvas">

  <section class="card card-front" aria-label="Card front">
    <div class="front-mark"></div>
    <div class="front-divider"></div>
    <div class="front-name">
      <div class="line-top">Halloway Crest</div>
      <div class="line-bottom">BACKERS GUILD</div>
    </div>
  </section>

  <section class="card card-back" aria-label="Card back">
    <svg class="back-wave" viewBox="0 0 520 297" preserveAspectRatio="none" aria-hidden="true">
      <path d="M0 252 C 120 205, 250 250, 380 220 C 450 204, 495 180, 520 160 L520 297 L0 297 Z" fill="var(--brand-green)"/>
      <path d="M0 232 C 110 196, 240 236, 370 206 C 420 194, 455 178, 478 164 C 450 186, 410 208, 370 218 C 240 250, 110 214, 0 248 Z" fill="var(--ink-dark)"/>
    </svg>

    <div class="back-brand">
      <span class="dot"></span>
      <span class="label">Halloway Crest Backers Guild</span>
    </div>

    <div class="holder">
      <div class="holder-name">DEAN VARROW</div>
      <div class="holder-title">Co-Founder / Investor</div>
    </div>

    <ul class="contact-list">
      <li>
        <svg viewBox="0 0 10 10"><path d="M2 0.5 L3.6 0.5 L4.2 3 L3 3.8 C3.6 5 4.8 6.3 6.2 7 L7 5.8 L9.5 6.4 L9.5 8 C9.5 9 8.8 9.5 8 9.5 C4 9.2 0.8 6 0.5 2 C0.5 1.2 1 0.5 2 0.5 Z" fill="var(--brand-green)"/></svg>
        555-314-2706
      </li>
      <li>
        <svg viewBox="0 0 10 10"><rect x="0.5" y="2" width="9" height="6.5" fill="var(--brand-green)"/><path d="M0.8 2.3 L5 5.6 L9.2 2.3" stroke="#fff" stroke-width="0.9" fill="none"/></svg>
        deanvarrow@mailtern.net
      </li>
      <li>
        <svg viewBox="0 0 10 10"><circle cx="5" cy="5" r="4.5" fill="var(--brand-green)"/><path d="M0.8 5 H9.2 M5 0.6 C3 3 3 7 5 9.4 M5 0.6 C7 3 7 7 5 9.4" stroke="#fff" stroke-width="0.7" fill="none"/></svg>
        www.hcbackersguild.com
      </li>
    </ul>
  </section>

</main>
</body>
</html>
```